LWTrendco

I ran out of business cards I designed myself on line. THe company went out of business and I LOVE my card. I am hoping someone can recreate the look or something equally as appealing to me.

Industry/Entity Type

Business

Colors
ecdaeb
f7f1f7

Requirements
Must have
• The card is going to be printed by a company Quibzo.com. they are very high end stock and I market to high end clients…the logo needs to remain small and centered at the top. If it helps my web site is lwtrendco.net you can see there how I left the logo very small

```html
<!DOCTYPE html>
<html lang="en">
<head>
<meta charset="utf-8">
<title>LW Trendco, LLC – Business Card</title>
<link rel="stylesheet" href="https://fonts.googleapis.com/css2?family=Cinzel:wght@400&display=swap">
<style>
  :root {
    --backdrop: #e6e7e9;
    --card-border: #e6c3dd;
    --card-paper: #fffffa;
    --ink-brown: #9a6a3f;
  }
  * { margin: 0; padding: 0; box-sizing: border-box; }
  html, body {
    width: 1200px;
    height: 1000px;
    overflow: hidden;
    background: var(--backdrop);
  }
  .canvas {
    position: relative;
    width: 1200px;
    height: 1000px;
  }
  .business-card {
    position: absolute;
    left: 379px;
    top: 163px;
    width: 442px;
    height: 674px;
    background: var(--card-border);
    padding: 15px 16px;
  }
  .card-face {
    position: relative;
    width: 100%;
    height: 100%;
    background: var(--card-paper);
    font-family: "Cinzel", "Times New Roman", serif;
    color: var(--ink-brown);
    text-align: center;
  }
  .brand-mark {
    position: absolute;
    left: 85px;
    top: 47px;
    width: 240px;
    height: 205px;
    display: flex;
    align-items: center;
    justify-content: center;
    font-size: 28px;
    letter-spacing: 1px;
  }
  .company-name {
    position: absolute;
    left: 0;
    right: 0;
    top: 262px;
    font-size: 36px;
    font-weight: 400;
    letter-spacing: 1px;
  }
  .tagline {
    position: absolute;
    left: 0;
    right: 0;
    top: 372px;
    font-size: 25px;
    letter-spacing: 1px;
  }
  .contact {
    position: absolute;
    left: 0;
    right: 0;
    top: 483px;
    font-size: 25px;
    line-height: 40px;
    letter-spacing: 0.5px;
    font-style: normal;
  }
</style>
</head>
<body>
  <div class="canvas">
    <div class="business-card">
      <div class="card-face">
        <div class="brand-mark" role="img" aria-label="LWTrendco logo">LWTrendco</div>
        <h1 class="company-name">LW Trendco, LLC</h1>
        <p class="tagline">Design &amp; Renovation</p>
        <address class="contact">
          <div class="contact-name">Colette Marven</div>
          <div class="contact-phone">410-555-0172</div>
          <div class="contact-email">colette@lwtrendco.net</div>
        </address>
      </div>
    </div>
  </div>
</body>
</html>
```